Marlow Crest Homes Needs Business Card Design

Looking for a unique modern business card to fit my new Logo.
Name: Dean Marlow
Company: Marlow Crest Homes, LLC
Tag Line: Forever Framed Right
Email: marlowcresthomes@mailvista.test
Phone: (253) 555-0187
Website: www.marlowcresthomes.test
License: MARLOCH462QT

```html
<!DOCTYPE html>
<html lang="en">
<head>
<meta charset="utf-8">
<title>Marlow Crest Homes – Business Card</title>
<link rel="stylesheet" href="https://fonts.googleapis.com/css2?family=Montserrat:wght@400;500;600;700&display=swap">
<style>
  :root {
    --backdrop: #3b3b3b;
    --card-dark: #141414;
    --card-light: #ffffff;
    --brand-blue: #2f93cf;
    --ink: #111111;
    --band-black: #050505;
  }
  * { margin: 0; padding: 0; box-sizing: border-box; }
  html, body {
    width: 900px; height: 1200px; overflow: hidden;
    background: var(--backdrop);
    font-family: "Montserrat", sans-serif;
  }
  .stage { position: relative; width: 900px; height: 1200px; }

  /* Front side */
  .card-front {
    position: absolute; left: 118px; top: 200px;
    width: 664px; height: 380px;
    background: var(--card-dark);
    overflow: hidden;
  }
  .card-front__pattern {
    position: absolute; inset: 0;
    background: linear-gradient(90deg, #0c0c0c 0%, #161616 45%, #3a3a3a 100%);
  }
  .card-front__name {
    position: absolute; left: 0; right: 0; top: 168px;
    text-align: center;
    color: #ffffff;
    font-weight: 700; font-size: 26px; letter-spacing: 1px;
    text-transform: uppercase;
  }

  /* Back side */
  .card-back {
    position: absolute; left: 123px; top: 620px;
    width: 655px; height: 376px;
    background: var(--card-light);
    overflow: hidden;
  }
  .contact { position: absolute; left: 43px; top: 98px; }
  .contact__name {
    color: var(--brand-blue);
    font-weight: 600; font-size: 27px; letter-spacing: 1px;
    line-height: 1;
    text-transform: uppercase;
  }
  .contact__role {
    margin-top: 6px;
    font-size: 15px; color: var(--ink); letter-spacing: 0.5px;
  }
  .contact__rule {
    width: 56px; height: 2px; background: var(--brand-blue);
    margin-top: 3px; margin-bottom: 9px;
  }
  .contact__line {
    display: flex; align-items: center; gap: 7px;
    font-size: 15px; color: var(--ink); letter-spacing: 0.4px;
    height: 24px;
  }
  .contact__line--phone { letter-spacing: 2.5px; }
  .contact__icon { width: 15px; height: 15px; flex: none; }
  .contact__license { margin-top: 6px; }
  .contact__label { color: var(--brand-blue); font-weight: 500; }

  .brand-mark {
    position: absolute; left: 400px; top: 196px; width: 200px;
    text-align: center;
    color: var(--ink);
    font-weight: 700; font-size: 24px; line-height: 1.15;
    text-transform: uppercase;
  }

  .tagline {
    position: absolute; left: 0; right: 0; top: 311px;
    text-align: center;
    color: var(--brand-blue);
    font-weight: 600; font-size: 18px; letter-spacing: 0.6px;
    text-transform: uppercase;
  }

  .base-band { position: absolute; left: 0; bottom: 0; width: 655px; height: 17px; }
</style>
</head>
<body>
<main class="stage">

  <section class="card-front" aria-label="Card front">
    <div class="card-front__pattern" role="img" aria-label="Repeating embossed brand pattern fading from black to grey"></div>
    <div class="card-front__name">Marlow Crest Homes</div>
  </section>

  <section class="card-back" aria-label="Card back">
    <div class="contact">
      <h1 class="contact__name">Dean Marlow</h1>
      <p class="contact__role">Owner</p>
      <div class="contact__rule"></div>

      <p class="contact__line contact__line--phone">
        <svg class="contact__icon" viewBox="0 0 24 24" aria-hidden="true"><path fill="#2f93cf" d="M6.6 10.8a15.1 15.1 0 0 0 6.6 6.6l2.2-2.2a1 1 0 0 1 1-.25 11.4 11.4 0 0 0 3.6.57 1 1 0 0 1 1 1V20a1 1 0 0 1-1 1A17 17 0 0 1 3 4a1 1 0 0 1 1-1h3.5a1 1 0 0 1 1 1c0 1.25.2 2.45.57 3.57a1 1 0 0 1-.25 1z"/></svg>
        (253) 555-0187
      </p>
      <p class="contact__line">
        <svg class="contact__icon" viewBox="0 0 24 24" aria-hidden="true"><rect x="2" y="5" width="20" height="14" fill="#2f93cf"/><path d="M2 5l10 8 10-8" fill="none" stroke="#fff" stroke-width="1.6"/><path d="M2 19l7-6M22 19l-7-6" stroke="#fff" stroke-width="1.2"/></svg>
        marlowcresthomes@mailvista.test
      </p>
      <p class="contact__line">
        <svg class="contact__icon" viewBox="0 0 24 24" aria-hidden="true"><g fill="none" stroke="#2f93cf" stroke-width="1.8"><circle cx="12" cy="12" r="9.5"/><ellipse cx="12" cy="12" rx="4" ry="9.5"/><path d="M2.5 12h19M4 7h16M4 17h16"/></g></svg>
        www.marlowcresthomes.test
      </p>
      <p class="contact__line contact__license">
        <span class="contact__label">License:</span> MARLOCH462QT
      </p>
    </div>

    <div class="brand-mark">Marlow Crest Homes</div>

    <p class="tagline">Forever Framed Right</p>

    <svg class="base-band" viewBox="0 0 655 17" aria-hidden="true">
      <polygon points="0,0 323,0 313,17 0,17" fill="#050505"/>
      <polygon points="333,0 655,0 655,17 323,17" fill="#2f93cf"/>
    </svg>
  </section>

</main>
</body>
</html>
```